Yard Sign Design for luxury design & build company

Looking to have 18" x 24" company yard signs designed.
An update to the business logo might be helpful.
Photos are not necessary but use if you can make inspiring.

Industry: Construction

Looking for a large headline of "Basement Finishing"
Website: www.tamberlyhomes.com
Phone Number (612) 555-0174
FB link: facebook.com/tamberlyhomesmn
Instagram: www.instagram.com/tamberlyhomesmn

Industry/Entity Type

Construction

Colors

Designer to choose colors to be used in the design.

Requirements
Must have
• Impactful high end characteristics
Nice to have
• Depth and detail graphis

```html
<!DOCTYPE html>
<html lang="en">
<head>
<meta charset="utf-8">
<title>Tamberly Homes – Basement Finishing Yard Sign</title>
<link rel="stylesheet" href="https://fonts.googleapis.com/css2?family=Montserrat:wght@700;800;900&display=swap">
<style>
  :root {
    --sign-black: #0a0b0c;
    --brand-red: #d3261f;
    --photo-red: #d9463c;
    --photo-red-deep: #b62a22;
    --white: #ffffff;
    --ink: #3b3b3b;
    --star-gold: #f7c21b;
    --backdrop: #d9d9d9;
  }
  * { box-sizing: border-box; margin: 0; padding: 0; }
  html, body {
    width: 676px; height: 1200px; overflow: hidden;
    background: var(--backdrop);
    font-family: "Montserrat", Arial, sans-serif;
  }
  .yard-sign {
    position: absolute; left: 28px; top: 367px;
    width: 620px; height: 465px;
    background: var(--white);
    box-shadow: 0 3px 8px rgba(0,0,0,.25);
    overflow: hidden;
  }
  .sign-graphics { position: absolute; inset: 0; }

  .brand {
    position: absolute; top: 22px; left: 0; right: 0;
    display: flex; align-items: center; justify-content: center; gap: 14px;
  }
  .brand-mark {
    width: 62px; height: 62px; border-radius: 50%;
    border: 3px solid var(--brand-red);
  }
  .brand-name {
    color: var(--white); font-weight: 800; font-size: 30px;
    letter-spacing: 3px; line-height: 1;
  }

  .headline {
    position: absolute; top: 160px; left: 0; right: 0;
    text-align: center; color: var(--white); font-weight: 900; line-height: .92;
  }
  .headline-top { display: block; font-size: 52px; letter-spacing: 1px; }
  .headline-main { display: block; font-size: 75px; }

  .contact {
    position: absolute; left: 40px; top: 355px; width: 256px; text-align: right;
  }
  .contact-phone { color: var(--brand-red); font-weight: 900; font-size: 33px; line-height: 1; }
  .contact-web { color: var(--ink); font-weight: 800; font-size: 15.5px; margin-top: 8px; }
  .contact-social { color: var(--ink); font-weight: 800; font-size: 17.5px; margin-top: 5px; }

  .divider {
    position: absolute; left: 309px; top: 354px; width: 2px; height: 88px;
    background: var(--ink);
  }

  .rating { position: absolute; left: 330px; top: 356px; width: 250px; }
  .rating-head { display: flex; align-items: center; gap: 12px; }
  .rating-badge { width: 46px; height: 46px; border-radius: 50%; background: #4a86e8; flex: none; }
  .rating-label { color: var(--ink); font-weight: 800; font-size: 17px; line-height: 1.15; }
  .rating-score { display: flex; align-items: center; gap: 4px; margin-top: 4px; }
  .rating-value { color: var(--ink); font-weight: 900; font-size: 32px; line-height: 1; }
  .rating-stars { width: 170px; height: 30px; }
</style>
</head>
<body>
  <div class="yard-sign">
    <svg class="sign-graphics" viewBox="0 0 620 465" aria-hidden="true">
      <defs>
        <linearGradient id="photoFill" x1="0" y1="0" x2="1" y2="1">
          <stop offset="0" stop-color="#c8372f"/>
          <stop offset=".5" stop-color="#dc4a40"/>
          <stop offset="1" stop-color="#b32a22"/>
        </linearGradient>
      </defs>
      <!-- header band -->
      <rect x="0" y="0" width="620" height="150" fill="var(--sign-black)"/>
      <!-- interior photo area -->
      <path d="M0 140 Q320 170 620 125 V335 Q330 300 0 338 Z" fill="url(#photoFill)" role="img" aria-label="Finished basement interior photo in red tone"/>
      <!-- white swoosh under header -->
      <path d="M0 112 Q300 150 620 110 V125 Q320 165 0 140 Z" fill="var(--white)"/>
      <!-- red accent under header -->
      <path d="M140 128 Q420 138 620 98 V110 Q380 150 140 128 Z" fill="var(--brand-red)"/>
      <!-- footer swooshes -->
      <path d="M0 330 Q330 296 620 330 V340 Q320 318 0 346 Z" fill="var(--white)"/>
      <path d="M0 346 Q320 318 620 340 V465 H0 Z" fill="var(--white)"/>
      <path d="M180 340 Q450 312 620 350 V362 Q450 322 180 340 Z" fill="var(--sign-black)"/>
    </svg>

    <div class="brand">
      <span class="brand-mark"></span>
      <span class="brand-name">TAMBERLY HOMES</span>
    </div>

    <h1 class="headline">
      <span class="headline-top">BASEMENT</span>
      <span class="headline-main">FINISHING</span>
    </h1>

    <div class="contact">
      <p class="contact-phone">612-555-0174</p>
      <p class="contact-web">www.tamberlyhomes.com</p>
      <p class="contact-social">tamberlyhomesmn</p>
    </div>

    <div class="divider"></div>

    <div class="rating">
      <div class="rating-head">
        <span class="rating-badge"></span>
        <p class="rating-label">Homeview<br>Business Review</p>
      </div>
      <div class="rating-score">
        <span class="rating-value">5.0</span>
        <svg class="rating-stars" viewBox="0 0 170 30" role="img" aria-label="Five star rating">
          <defs>
            <path id="star" d="M15 1 L18.5 11 H29 L20.5 17.5 L23.7 28 L15 21.5 L6.3 28 L9.5 17.5 L1 11 H11.5 Z" fill="var(--star-gold)"/>
          </defs>
          <use href="#star" x="0"/>
          <use href="#star" x="34"/>
          <use href="#star" x="68"/>
          <use href="#star" x="102"/>
          <use href="#star" x="136"/>
        </svg>
      </div>
    </div>
  </div>
</body>
</html>
```